Stationary and Business Card for dental office
Velbrook Endodontics
Stationary and Business Card for dental office  - Health
Creative Brief
Use same font as used in my logo
use any font that is easy to read. should go with font in the logo
Professional
Miren T. Osbury, D.D.S.
418 Pelloway Court, Suite #1 Dunmere, CA 90210
info@velbrookendo.example
www.velbrookendo.example
Business card should have 2 logos, one brown and gold one with a tooth image....that is my main logo. The second logo( the one that says pdrcertified member) which I have uploaded as well can be in a corner or anywhere on the card. basically it is your choice where it goes on the card. It does not have to be the same size as my main business logo. This second logo only needs to be on the business cards. it can be black and white or color. I will leave that decision to you so if you think the colored logo goes with my logo colors, then use that. If not then, use the black and white one. I will prefer it in color. Under my name on business card, please write the following in smaller font Practice Limited to Endodontics LETTER HEAD: deisgn does not need to have the second logo (pdrcertifeid member logo). It should have my main business logo ( gold and brown one) with business name and all the other info like address, phone, fax web/email. ENVELOPE: only main business logo with business name and address. Please do not include phone/fax/ email or any other logos on the envelope. Thank you.

```html
<!DOCTYPE html>
<html lang="en">
<head>
<meta charset="utf-8">
<title>Velbrook Endodontics – Business Card</title>
<link rel="stylesheet" href="https://fonts.googleapis.com/css2?family=Encode+Sans+Semi+Condensed:wght@400;500&family=Open+Sans:ital,wght@0,400;0,600;1,400&display=swap">
<style>
  :root {
    --brown: #4a2c22;
    --gold: #d9b183;
    --ink: #3b3b3b;
    --rule: #9a9a9a;
    --card: #ffffff;
    --backdrop: #d8d9db;
    --backdrop-light: #eeeff0;
  }
  * { margin: 0; padding: 0; box-sizing: border-box; }
  html, body { width: 1200px; height: 987px; overflow: hidden; }
  body {
    background: radial-gradient(circle at 50% 40%, var(--backdrop-light), var(--backdrop));
    font-family: "Open Sans", Arial, sans-serif;
    color: var(--ink);
    position: relative;
  }
  .card {
    position: absolute;
    left: 220px;
    width: 760px;
    height: 434px;
    background: var(--card);
    border-radius: 28px;
    overflow: hidden;
    box-shadow: 0 12px 30px rgba(0,0,0,.18);
  }
  .card--back { top: 40px; }
  .card--front { top: 513px; }

  /* back side */
  .back-mark {
    position: absolute;
    left: 0; right: 0; top: 120px;
    display: flex; flex-direction: column; align-items: center; gap: 16px;
  }
  .brand-dot {
    width: 96px; height: 96px; border-radius: 50%;
    background: var(--brown);
  }
  .brand-name {
    font-family: "Encode Sans Semi Condensed", Arial, sans-serif;
    font-weight: 400;
    color: var(--brown);
    white-space: nowrap;
  }
  .back-mark .brand-name { font-size: 30px; }
  .back-url {
    position: absolute; left: 0; right: 0; top: 318px;
    text-align: center;
    font-size: 17px; letter-spacing: 3px;
    font-style: italic;
    color: var(--ink);
  }

  /* front side */
  .waves { position: absolute; inset: 0; }
  .front-head {
    position: absolute; left: 150px; top: 54px;
    display: flex; align-items: center; gap: 16px;
  }
  .front-head .brand-dot { width: 70px; height: 70px; }
  .front-head .brand-name { font-size: 42px; }
  .details {
    position: absolute; left: 190px; top: 150px;
    display: flex; gap: 24px;
    font-size: 14px; line-height: 1.55;
    white-space: nowrap;
  }
  .practitioner { text-align: right; }
  .practitioner .name { font-weight: 600; font-size: 15px; margin-bottom: 6px; }
  .divider { width: 1px; background: var(--rule); }
  .contacts { list-style: none; }
  .contacts li { display: flex; align-items: center; gap: 8px; }
  .contacts svg { width: 12px; height: 12px; flex: none; }
</style>
</head>
<body>

  <section class="card card--back" aria-label="Business card back">
    <div class="back-mark">
      <span class="brand-dot"></span>
      <span class="brand-name">Velbrook Endodontics</span>
    </div>
    <p class="back-url">www.velbrookendo.example</p>
  </section>

  <section class="card card--front" aria-label="Business card front">
    <svg class="waves" viewBox="0 0 760 434" preserveAspectRatio="none" aria-hidden="true">
      <path d="M0 210 C 120 250, 260 300, 420 340 C 560 372, 680 390, 760 392 L760 434 L0 434 Z" fill="var(--gold)"/>
      <path d="M0 232 C 130 270, 260 316, 420 352 C 560 382, 680 398, 760 400 L760 434 L0 434 Z" fill="var(--card)"/>
      <path d="M0 244 C 130 284, 270 330, 430 364 C 570 392, 690 408, 760 410 L760 434 L0 434 Z" fill="var(--brown)"/>
    </svg>

    <header class="front-head">
      <span class="brand-dot"></span>
      <span class="brand-name">Velbrook Endodontics</span>
    </header>

    <div class="details">
      <div class="practitioner">
        <p class="name">Miren T. Osbury, D.D.S.</p>
        <p>418 Pelloway Court, Suite #1</p>
        <p>Dunmere, CA 90210</p>
      </div>
      <span class="divider"></span>
      <ul class="contacts">
        <li><svg viewBox="0 0 12 12"><circle cx="6" cy="6" r="6" fill="var(--brown)"/></svg>555-014-2291</li>
        <li><svg viewBox="0 0 12 12"><circle cx="6" cy="6" r="6" fill="var(--brown)"/></svg>555-014-6673</li>
        <li><svg viewBox="0 0 12 12"><circle cx="6" cy="6" r="6" fill="var(--brown)"/></svg>info@velbrookendo.example</li>
        <li><svg viewBox="0 0 12 12"><circle cx="6" cy="6" r="6" fill="var(--brown)"/></svg>www.velbrookendo.example</li>
      </ul>
    </div>
  </section>

</body>
</html>
```